Business card for new business - financial management

I need a business card designed for my new business. I'm the owner / sole trader of TVH Consulting, which provides financial management services for Government. I'd like the design to incorporate the attached business name and colours. The design should include colour and not be too way out - it needs to look at home in a government environment.
Details to be included on the card are:
TVH Consulting
Delia Ravick
0400 938 214
deliaeravick@mailbrook.net
47 Pellham Crescent, Marrowby ACT 2619
Single or double sided designs would be good.
Target Market(s)
Employees at Australian Federal Government agencies
Industry/Entity Type
Government
Look and feel

```html
<!DOCTYPE html>
<html lang="en">
<head>
<meta charset="utf-8">
<title>TVH Consulting – Business Card</title>
<link rel="stylesheet" href="https://fonts.googleapis.com/css2?family=Fira+Sans:ital,wght@0,300;0,400;0,600;1,300&display=swap">
<style>
  :root {
    --page-bg: #e9ebee;
    --card-white: #ffffff;
    --band-blue: #2f5c9c;
    --accent-aqua: #7cc3d6;
    --brand-teal: #1f6a7c;
    --text-light: #e6eef8;
    --card-shadow: rgba(20, 40, 70, 0.18);
  }
  * { margin: 0; padding: 0; box-sizing: border-box; }
  html, body {
    width: 1200px;
    height: 873px;
    overflow: hidden;
    background: var(--page-bg);
    font-family: "Fira Sans", Arial, sans-serif;
  }
  .canvas {
    position: relative;
    width: 1200px;
    height: 873px;
    display: flex;
    align-items: center;
    justify-content: center;
  }
  .business-card {
    position: relative;
    width: 900px;
    height: 550px;
    background: var(--card-white);
    box-shadow: 0 12px 36px var(--card-shadow);
    overflow: hidden;
  }
  .card-bands {
    position: absolute;
    inset: 0;
    width: 100%;
    height: 100%;
  }
  .brand {
    position: absolute;
    left: 0;
    right: 0;
    top: 150px;
    display: flex;
    align-items: center;
    justify-content: center;
    gap: 18px;
  }
  .brand-mark {
    width: 22px;
    height: 22px;
    background: var(--brand-teal);
  }
  .brand-name {
    font-weight: 400;
    font-size: 64px;
    letter-spacing: 1px;
    color: var(--brand-teal);
  }
  .contact {
    position: absolute;
    left: 0;
    right: 0;
    top: 395px;
    text-align: center;
    color: var(--text-light);
    font-weight: 300;
    font-size: 24px;
    line-height: 1.45;
  }
  .contact-name {
    font-weight: 600;
    color: #ffffff;
  }
  .contact-role {
    font-style: italic;
    font-weight: 300;
    font-size: 20px;
  }
</style>
</head>
<body>
  <main class="canvas">
    <article class="business-card">
      <svg class="card-bands" viewBox="0 0 900 550" aria-hidden="true">
        <path d="M0 0 H900 V22 Q450 70 0 42 Z" fill="var(--band-blue)"/>
        <path d="M0 42 Q450 70 900 22 L900 30 Q450 80 0 50 Z" fill="var(--accent-aqua)"/>
        <path d="M0 360 Q420 330 900 420 L900 408 Q420 316 0 346 Z" fill="var(--accent-aqua)"/>
        <path d="M0 370 Q420 342 900 430 V550 H0 Z" fill="var(--band-blue)"/>
      </svg>

      <div class="brand">
        <span class="brand-mark"></span>
        <span class="brand-name">TVH Consulting</span>
      </div>

      <div class="contact">
        <p><span class="contact-name">Delia Ravick</span> <span class="contact-role">- Owner</span></p>
        <p>47 Pellham Crescent, Marrowby ACT 2619</p>
        <p>Phone: 0400 938 214 | Email: deliaeravick@mailbrook.net</p>
      </div>
    </article>
  </main>
</body>
</html>
```